Marrow Creek 381 Wine Label

Marrow Creek 381 Wine bottle label-
Pinot Noir, Chardonnay. Premium label.
Startup vineyard, Cool climate, Tasmania Australia.
Hills and Valley area, South East location
Needs to be a front and rear label as there are label requirements in Australia. Rear lable
is mearly to talk about the wine and have required information as per the examples uploaded

```html
<!DOCTYPE html>
<html lang="en">
<head>
<meta charset="utf-8">
<title>Marrow Creek 381 Wine Labels</title>
<link rel="stylesheet" href="https://fonts.googleapis.com/css2?family=Jost:wght@300;400&family=Mrs+Saint+Delafield&display=swap">
<style>
  :root {
    --page: #ffffff;
    --ink: #ffffff;
    --pinot-top: #1b2658;
    --pinot-mid: #4d3482;
    --pinot-low: #9a619f;
    --pinot-base: #cd7399;
    --chard-top: #0e6db4;
    --chard-sky: #2a88c9;
    --chard-hill: #3e9898;
    --chard-low: #7dba78;
    --chard-base: #7cbb50;
  }
  * { margin: 0; padding: 0; box-sizing: border-box; }
  html, body {
    width: 1200px;
    height: 848px;
    overflow: hidden;
    background: var(--page);
  }
  .sheet {
    position: relative;
    width: 1200px;
    height: 848px;
  }
  .label {
    position: absolute;
    top: 193px;
    width: 321px;
    height: 460px;
    color: var(--ink);
    text-align: center;
  }
  .label--pinot { left: 218px; }
  .label--chardonnay { left: 636px; }
  .label__scene {
    position: absolute;
    inset: 0;
    width: 100%;
    height: 100%;
    display: block;
  }
  .label__brand {
    position: absolute;
    top: 52px;
    left: 88px;
    width: 145px;
    height: 144px;
    display: flex;
    align-items: center;
    justify-content: center;
    font-family: "Jost", sans-serif;
    font-weight: 300;
    font-size: 22px;
    line-height: 1.25;
    letter-spacing: 0.08em;
    text-transform: uppercase;
  }
  .label__region {
    position: absolute;
    top: 245px;
    left: 0;
    width: 100%;
    font-family: "Jost", sans-serif;
    font-weight: 300;
    font-size: 15px;
    letter-spacing: 0.09em;
  }
  .label__variety {
    position: absolute;
    top: 262px;
    left: 0;
    width: 100%;
    font-family: "Mrs Saint Delafield", cursive;
    font-size: 54px;
    line-height: 1.2;
  }
  .label__vintage {
    position: absolute;
    top: 334px;
    left: 0;
    width: 100%;
    font-family: "Jost", sans-serif;
    font-weight: 300;
    font-size: 20px;
    letter-spacing: 0.03em;
  }
  .label__origin {
    position: absolute;
    top: 408px;
    left: 0;
    width: 100%;
    font-family: "Jost", sans-serif;
    font-weight: 300;
    font-size: 14.5px;
    letter-spacing: 0.07em;
  }
</style>
</head>
<body>
<main class="sheet">

  <section class="label label--pinot">
    <svg class="label__scene" viewBox="0 0 321 460" preserveAspectRatio="none" role="img" aria-label="Layered misty mountain range reflected in still water, in violet and pink tones">
      <defs>
        <linearGradient id="pinot-fade" x1="0" y1="0" x2="0" y2="1">
          <stop offset="0" stop-color="var(--pinot-top)"/>
          <stop offset="0.5" stop-color="var(--pinot-mid)"/>
          <stop offset="0.75" stop-color="var(--pinot-low)"/>
          <stop offset="1" stop-color="var(--pinot-base)"/>
        </linearGradient>
      </defs>
      <rect width="321" height="460" fill="url(#pinot-fade)"/>
    </svg>
    <div class="label__brand">Marrow Creek<br>381</div>
    <p class="label__region">COAL RIVER VALLEY</p>
    <p class="label__variety">Pinot Noir</p>
    <p class="label__vintage">2025</p>
    <p class="label__origin">Wine of Australia</p>
  </section>

  <section class="label label--chardonnay">
    <svg class="label__scene" viewBox="0 0 321 460" preserveAspectRatio="none" role="img" aria-label="Layered misty mountain range reflected in still water, in blue and green tones">
      <defs>
        <linearGradient id="chard-fade" x1="0" y1="0" x2="0" y2="1">
          <stop offset="0" stop-color="var(--chard-top)"/>
          <stop offset="0.3" stop-color="var(--chard-sky)"/>
          <stop offset="0.55" stop-color="var(--chard-hill)"/>
          <stop offset="0.78" stop-color="var(--chard-low)"/>
          <stop offset="1" stop-color="var(--chard-base)"/>
        </linearGradient>
      </defs>
      <rect width="321" height="460" fill="url(#chard-fade)"/>
    </svg>
    <div class="label__brand">Marrow Creek<br>381</div>
    <p class="label__region">COAL RIVER VALLEY</p>
    <p class="label__variety">Chardonnay</p>
    <p class="label__vintage">2025</p>
    <p class="label__origin">Wine of Australia</p>
  </section>

</main>
</body>
</html>
```